Flyer Template

I need a flyer template for door knocking on properties. Text Boxes need to be editable, with a header and text body. Footer to be my info. Project to be stylized to match my real estate signs and logo art from past projects

```html
<!DOCTYPE html>
<html lang="en">
<head>
<meta charset="utf-8">
<title>Door Knocking Flyer</title>
<link rel="stylesheet" href="https://fonts.googleapis.com/css2?family=Montserrat:ital,wght@0,500;0,600;0,700;1,500&display=swap">
<style>
  :root {
    --stage: #1c1c1e;
    --white: #ffffff;
    --red: #e21f26;
    --red-deep: #9a1a20;
    --orange: #f7a83a;
    --ink: #111111;
    --sky-top: #8fb4d8;
    --sky-mid: #c9cfd2;
    --lawn: #6a9445;
  }
  * { margin: 0; padding: 0; box-sizing: border-box; }
  html, body { width: 927px; height: 1200px; overflow: hidden; background: var(--stage); }
  body { position: relative; font-family: 'Montserrat', sans-serif; }

  .flyer {
    position: absolute; left: 110px; top: 143px;
    width: 706px; height: 914px; overflow: hidden; background: var(--white);
  }
  .flyer-shapes { position: absolute; inset: 0; width: 706px; height: 914px; }

  .brand { position: absolute; left: 494px; top: 46px; width: 200px; text-align: center; }
  .brand-mark { display: block; width: 34px; height: 34px; margin: 0 auto 28px; background: var(--red); }
  .brand-name { font-weight: 700; font-size: 27px; line-height: 30px; color: var(--ink); letter-spacing: 0.5px; }

  .price { position: absolute; left: 462px; top: 364px; width: 200px; text-align: center; color: var(--white); }
  .price-label { font-weight: 700; font-size: 19px; letter-spacing: 1.5px; line-height: 22px; }
  .price-value { font-weight: 700; font-size: 38px; line-height: 44px; }

  .headline { position: absolute; left: 44px; top: 458px; color: var(--white); font-weight: 600; }
  .headline-lead { font-size: 44px; line-height: 50px; }
  .headline-title { font-size: 59px; line-height: 62px; font-weight: 700; color: var(--orange); }
  .headline-slogan { font-size: 38px; line-height: 48px; font-weight: 600; }

  .info-columns { position: absolute; left: 44px; top: 636px; display: flex; gap: 22px; }
  .info-block { width: 190px; color: var(--white); }
  .info-title { font-weight: 600; font-size: 21px; line-height: 22px; }
  .info-body { font-weight: 500; font-size: 12.6px; line-height: 15.3px; }

  .page-dots { position: absolute; left: 44px; top: 866px; display: flex; gap: 18px; }
  .page-dots span { width: 26px; height: 16px; background: var(--white); }
  .page-dots span.is-active { background: var(--orange); }

  .contact { position: absolute; right: 32px; top: 830px; text-align: right; color: var(--red); }
  .contact-call { position: relative; padding-left: 44px; display: inline-block; text-align: left; }
  .contact-icon { position: absolute; left: 0; top: 4px; width: 34px; height: 34px; }
  .contact-label { font-weight: 700; font-size: 13.5px; line-height: 16px; }
  .contact-phone { font-weight: 700; font-size: 21px; line-height: 24px; letter-spacing: 0.5px; }
  .contact-email { font-weight: 500; font-style: italic; font-size: 20.5px; line-height: 26px; letter-spacing: 0.5px; margin-top: 2px; }
</style>
</head>
<body>
<main class="flyer">
  <svg class="flyer-shapes" viewBox="0 0 883 1142" preserveAspectRatio="none">
    <defs>
      <linearGradient id="photoTone" x1="0" y1="0" x2="0" y2="1">
        <stop offset="0" stop-color="var(--sky-top)"/>
        <stop offset="0.55" stop-color="var(--sky-mid)"/>
        <stop offset="1" stop-color="var(--lawn)"/>
      </linearGradient>
      <linearGradient id="redTone" x1="0" y1="0" x2="1" y2="0.4">
        <stop offset="0" stop-color="var(--red-deep)"/>
        <stop offset="1" stop-color="var(--red)"/>
      </linearGradient>
    </defs>
    <rect class="property-photo" role="img" aria-label="Photo of a two-storey house with a carport and front lawn" x="0" y="0" width="883" height="640" fill="url(#photoTone)"/>
    <path d="M478,0 C520,130 650,240 883,222 L883,0 Z" fill="var(--white)"/>
    <path d="M330,570 C450,450 620,412 883,410 L883,700 L330,700 Z" fill="url(#redTone)"/>
    <path d="M0,473 C180,462 330,540 430,600 C500,640 560,640 640,600 C720,565 800,556 883,558 L883,1142 L0,1142 Z" fill="url(#redTone)"/>
    <path d="M0,473 C180,462 330,540 430,600 C500,640 560,640 640,600 C720,565 800,556 883,558" fill="none" stroke="var(--white)" stroke-width="4"/>
    <path d="M397,1142 C500,1040 700,1000 883,1000 L883,1142 Z" fill="var(--white)"/>
  </svg>

  <div class="brand">
    <span class="brand-mark"></span>
    <div class="brand-name">MARREN<br>REALTY</div>
  </div>

  <div class="price">
    <div class="price-label">TEXT HER</div>
    <div class="price-value">$000,00</div>
  </div>

  <div class="headline">
    <div class="headline-lead">YOUR</div>
    <div class="headline-title">TITLE HERE</div>
    <div class="headline-slogan">YOUR SALOGAN HERE</div>
  </div>

  <div class="info-columns">
    <div class="info-block">
      <h3 class="info-title">Text Here:</h3>
      <p class="info-body">Lorem ipsum dolor sit amet, consectetuer adipiscing elit, sed diam nonummy nibh euismod tincidunt ut laoreet dolore magna aliquam erat volutpat. Ut wisi enim ad minim veniam, quis nostrud exerci tation ullamcorper suscipit lobortis</p>
    </div>
    <div class="info-block">
      <h3 class="info-title">Text Here:</h3>
      <p class="info-body">Lorem ipsum dolor sit amet, consectetuer adipiscing elit, sed diam nonummy nibh euismod tincidunt ut laoreet dolore magna aliquam erat volutpat. Ut wisi enim ad minim veniam, quis nostrud exerci tation ullamcorper suscipit lobortis</p>
    </div>
    <div class="info-block">
      <h3 class="info-title">Text Here:</h3>
      <p class="info-body">Lorem ipsum dolor sit amet, consectetuer adipiscing elit, sed diam nonummy nibh euismod tincidunt ut laoreet dolore magna aliquam erat volutpat. Ut wisi enim ad minim veniam, quis nostrud exerci tation ullamcorper suscipit lobortis</p>
    </div>
  </div>

  <div class="page-dots"><span></span><span></span><span class="is-active"></span></div>

  <footer class="contact">
    <div class="contact-call">
      <svg class="contact-icon" viewBox="0 0 34 34">
        <circle cx="17" cy="17" r="17" fill="var(--red)"/>
        <path d="M10,10 h5 l1,5 -2,2 c1,2 2,3 4,4 l2,-2 5,1 v5 c-9,0 -15,-6 -15,-15 z" fill="var(--white)"/>
      </svg>
      <div class="contact-label">Call Now :</div>
      <div class="contact-phone">555-210-0148</div>
    </div>
    <div class="contact-email">jmarren@example.com</div>
  </footer>
</main>
</body>
</html>
```